Tarnholt Bright Press Label

We are looking for a label for our blueberry vodka and lemonade ready-to-drink cocktail. we would like the ingredients (vodka, lemon juice, cane sugar, blueberries) discretely displayed on the label. We would also like 15% alc/vol (30 proof) on the label. The label is for a 12-ounce slim can. We would also like the Surgeon Generals warning ion the label

Target Market(s)

Spike seltzer and ready to drink cocktail drinkers

Font styles to use
Decorative

Requirements
Must have
• Surgeon General warning, 15% alc/vol (30 proof) 12 ounces., Ingredients

```html
<!DOCTYPE html>
<html lang="en">
<head>
<meta charset="utf-8">
<title>Tarnholt Bright Press – Blueberry Vodka &amp; Lemonade Label</title>
<link href="https://fonts.googleapis.com/css2?family=Rye&family=Alfa+Slab+One&family=Lobster&family=IM+Fell+English&family=Arimo:wght@400;700&display=swap" rel="stylesheet">
<style>
  :root {
    --backdrop: #dde1e1;
    --sky-light: #b6cdee;
    --sky-mid: #8fb1e2;
    --navy: #1b1a80;
    --navy-deep: #15146b;
    --lemon: #f2c21b;
    --white: #ffffff;
    --ink: #1d1d1d;
    --band-light: #eceef2;
    --fine-print: #d9dcf2;
  }
  html, body {
    margin: 0;
    padding: 0;
    width: 1200px;
    height: 800px;
    overflow: hidden;
    background: var(--backdrop);
  }
  .canvas {
    width: 1200px;
    height: 800px;
    display: flex;
    align-items: center;
    justify-content: center;
  }
  .label { display: block; }
  .tagline { font-family: "Rye", serif; font-size: 14px; fill: var(--white); }
  .brand-name { font-family: "IM Fell English", serif; font-size: 19px; fill: var(--ink); }
  .flavour-main {
    font-family: "Rye", serif; font-size: 48px; fill: var(--navy);
    stroke: var(--white); stroke-width: 6px; paint-order: stroke; stroke-linejoin: round;
  }
  .flavour-spirit {
    font-family: "Alfa Slab One", serif; font-size: 44px; fill: var(--navy);
    stroke: var(--white); stroke-width: 6px; paint-order: stroke; stroke-linejoin: round;
  }
  .ampersand { font-family: "Alfa Slab One", serif; font-size: 32px; fill: var(--navy); }
  .flavour-mixer {
    font-family: "Lobster", cursive; font-size: 44px; fill: var(--lemon);
    stroke: var(--white); stroke-width: 6px; paint-order: stroke; stroke-linejoin: round;
  }
  .strength { font-family: "Arimo", sans-serif; font-size: 16px; fill: var(--white); }
  .ingredients { font-family: "Arimo", sans-serif; font-size: 9px; fill: var(--fine-print); }
  .volume { font-family: "Arimo", sans-serif; font-weight: 700; font-size: 24px; fill: var(--ink); }
  .volume-unit { font-size: 18px; }
  .warning { font-family: "Arimo", sans-serif; font-size: 6.5px; fill: var(--fine-print); }
  .warning-lead { font-weight: 700; }
</style>
</head>
<body>
<main class="canvas">
  <svg class="label" width="300" height="760" viewBox="0 0 300 760" xmlns="http://www.w3.org/2000/svg">
    <defs>
      <linearGradient id="sky" x1="0" y1="0" x2="0" y2="1">
        <stop offset="0" stop-color="var(--sky-light)"/>
        <stop offset="0.5" stop-color="var(--sky-mid)"/>
        <stop offset="1" stop-color="var(--sky-light)"/>
      </linearGradient>
      <linearGradient id="berries" x1="0" y1="0" x2="1" y2="1">
        <stop offset="0" stop-color="#5b9a3a"/>
        <stop offset="0.5" stop-color="#3b4aa0"/>
        <stop offset="1" stop-color="#22286a"/>
      </linearGradient>
    </defs>

    <rect class="sky" x="0" y="0" width="300" height="512" fill="url(#sky)" role="img" aria-label="Brush-stroke blue sky texture"/>

    <text class="tagline" x="150" y="35" text-anchor="middle">Ready to Drink Cocktail</text>

    <g class="brand">
      <circle cx="150" cy="142" r="50" fill="none" stroke="var(--white)" stroke-width="5"/>
      <text class="brand-name" x="150" y="137" text-anchor="middle">Tarnholt</text>
      <text class="brand-name" x="150" y="162" text-anchor="middle">Bright Press</text>
    </g>

    <text class="flavour-main" x="150" y="332" text-anchor="middle" textLength="288" lengthAdjust="spacingAndGlyphs">BLUEBERRY</text>
    <text class="flavour-spirit" x="150" y="398" text-anchor="middle" textLength="236" lengthAdjust="spacingAndGlyphs">VODKA</text>
    <text class="ampersand" x="150" y="468" text-anchor="middle">&amp;</text>

    <rect class="band-dark" x="0" y="512" width="300" height="152" fill="var(--navy)"/>

    <rect class="berries" x="0" y="410" width="42" height="104" rx="14" fill="url(#berries)" role="img" aria-label="Illustration of blueberries with green leaves"/>

    <text class="flavour-mixer" x="155" y="528" text-anchor="middle" transform="rotate(-8 155 516)">Lemonade</text>

    <text class="strength" x="150" y="610" text-anchor="middle">15% alc/vol (30 proof)</text>
    <text class="ingredients" x="150" y="640" text-anchor="middle">Ingredients: vodka, lemon juice, cane sugar, blueberries</text>

    <rect class="band-light" x="0" y="664" width="300" height="42" fill="var(--band-light)"/>
    <text class="volume" x="150" y="694" text-anchor="middle">12 <tspan class="volume-unit">fl.oz</tspan></text>

    <rect class="band-foot" x="0" y="706" width="300" height="54" fill="var(--navy-deep)"/>
    <g class="warning">
      <text x="150" y="720" text-anchor="middle"><tspan class="warning-lead">GOVERNMENT WARNING:</tspan> (1) According to the Surgeon General, women should not</text>
      <text x="150" y="729" text-anchor="middle">drink alcoholic beverages during pregnancy because of the risk of birth</text>
      <text x="150" y="738" text-anchor="middle">defects. (2) Consumption of alcoholic beverages impairs your ability to drive</text>
      <text x="150" y="747" text-anchor="middle">a car or operate machinery, and may cause health problems.</text>
    </g>
  </svg>
</main>
</body>
</html>
```